Postcard Design

THE BRAMBLEWOOD AGENCY--MORTGAGE; FINAL EXPENSE; COLLEGE FUNDS; FINANCIAL PLANNING; FEATURING DISABILITY INCOME RIDERS; ACCIDENTAL DEATH RIDERS; CHILDREN&GRANDCHILDREN RIDERS; LIVING DEATH BENEFIT RIDERS; WAIVE PREMIUM RIDERS; AND UNEMPLOYMENT RIDERS

IF INTERESTED AND WANT MORE DETAILS PLEASE CONTACT: MIRTA DOLLEN @ 555-417-2093

Industry/Entity Type

College

```html
<!DOCTYPE html>
<html lang="en">
<head>
<meta charset="utf-8">
<title>The Bramblewood Agency – Postcard</title>
<link href="https://fonts.googleapis.com/css2?family=Marcellus&family=Roboto+Condensed:wght@400;700&family=Open+Sans:wght@700;800&family=Arimo:wght@400&display=swap" rel="stylesheet">
<style>
:root{
  --blue:#0f5a98;
  --blue-light:#2f86c6;
  --charcoal:#3d3d3f;
  --orange:#f39a1e;
  --paper:#ffffff;
  --panel:#ededed;
  --ink:#555;
  --red:#d62828;
  --backdrop:#e6e2dc;
}
*{margin:0;padding:0;box-sizing:border-box}
html,body{width:825px;height:1200px;overflow:hidden}
body{background:var(--backdrop);position:relative;font-family:"Roboto Condensed",Arial,sans-serif}
.card{position:absolute;left:110px;width:607px;height:472px;background:var(--paper);overflow:hidden;box-shadow:0 3px 10px rgba(0,0,0,.25)}
.card--front{top:133px}
.card--back{top:672px;height:470px}
.abs{position:absolute}
.agency-name{font-family:"Marcellus",Georgia,serif;color:#fff;font-size:22px;letter-spacing:.2px;white-space:nowrap}
.headline{font-family:"Open Sans",Arial,sans-serif;font-weight:700;color:#fff;font-size:24px;letter-spacing:.2px;white-space:nowrap}
.website{font-family:"Arimo",Arial,sans-serif;color:var(--orange);font-size:18px;font-weight:400}
.contact{color:#fff;font-size:18px;line-height:22px}
.footer{position:absolute;left:0;right:0;bottom:0;height:42px;background:var(--charcoal);border-top:6px solid var(--orange);color:#fff;font-family:"Arimo",Arial,sans-serif;font-size:15px;line-height:36px;padding-left:30px;box-sizing:content-box}
.photo{position:absolute;border:3px solid var(--orange)}
.services{position:absolute;top:348px;display:grid;grid-template-columns:127px 126px 122px;left:218px;font-size:11px;color:var(--ink);line-height:15px}
.services ul{list-style:none}
.services li{position:relative;padding-left:10px}
.services li::before{content:"";position:absolute;left:0;top:5px;width:4px;height:4px;border-radius:50%;background:var(--red)}
.badge{position:absolute}
.badge-text{position:absolute;inset:0;display:flex;flex-direction:column;align-items:center;justify-content:center;font-family:"Open Sans",Arial,sans-serif;font-weight:800;color:var(--charcoal);line-height:1}
.stamp{position:absolute;left:510px;top:22px;width:72px;height:72px;background:#cfcfcf}
</style>
</head>
<body>

<section class="card card--front">
  <div class="abs" style="left:0;top:0;width:330px;height:85px;background:linear-gradient(180deg,var(--blue-light),var(--blue))"></div>
  <div class="abs agency-name" style="left:33px;top:38px">The Bramblewood Agency</div>
  <div class="abs" style="left:0;top:87px;width:330px;height:110px;background:var(--charcoal)"></div>
  <p class="abs contact" style="left:37px;top:107px">If interested and want more details<br>Please contact:<br>Mirta Dollen @ 555-417-2093</p>
  <div class="abs" style="left:0;top:200px;width:340px;height:82px;background:linear-gradient(180deg,var(--blue-light),var(--blue));border-bottom:4px solid var(--orange)"></div>
  <div class="abs headline" style="left:37px;top:214px">LOREM IPSUM</div>
  <div class="abs website" style="left:37px;top:245px">www.website.com</div>
  <div class="abs" style="left:0;top:286px;width:607px;height:136px;background:linear-gradient(180deg,#fff,var(--panel))"></div>

  <svg class="abs" style="left:0;top:0" width="607" height="310" viewBox="0 0 607 310">
    <defs>
      <linearGradient id="deskTones" x1="0" y1="0" x2="1" y2="1">
        <stop offset="0" stop-color="#eef1f4"/><stop offset=".5" stop-color="#b9c0c8"/><stop offset="1" stop-color="#dfe4ea"/>
      </linearGradient>
    </defs>
    <path d="M345 0 C322 60 312 150 338 218 C370 280 470 306 607 302" fill="none" stroke="var(--orange)" stroke-width="6"/>
    <path d="M352 0 C328 60 319 150 345 214 C376 274 470 298 607 295" fill="none" stroke="var(--blue)" stroke-width="5"/>
    <path role="img" aria-label="Photo: hands typing on a laptop beside a printed chart" d="M357 0 H607 V292 C470 295 380 272 350 212 C326 150 334 60 357 0 Z" fill="url(#deskTones)"/>
  </svg>

  <div class="badge" style="left:232px;top:234px;width:90px;height:90px">
    <svg width="90" height="90" viewBox="0 0 90 90"><circle cx="45" cy="45" r="41" fill="#fff" stroke="var(--blue-light)" stroke-width="3" stroke-dasharray="6 3"/><circle cx="45" cy="45" r="35" fill="#f4f4f4"/></svg>
    <div class="badge-text"><span style="font-size:14px">JOIN US</span><span style="font-size:19px">NOW!</span></div>
  </div>

  <div class="photo" role="img" aria-label="Photo: couple using a laptop on a sofa" style="left:22px;top:316px;width:176px;height:90px;background:linear-gradient(135deg,#8a8f96,#d9dcdf 60%,#a7acb2)"></div>

  <div class="services">
    <ul><li>Mortgage, final expense</li><li>College funds</li><li>Financial planning</li><li>Featuring disability</li></ul>
    <ul><li>Income riders</li><li>Accidental death riders</li><li>Children</li><li>Grandchildren riders</li></ul>
    <ul><li>Living death benefit riders</li><li>Waive premium riders</li><li>Unemployment riders</li></ul>
  </div>

  <footer class="footer">lorem ipsum dolor sit amrt | Phone: 123.466.78 | Email: lorem@mailnest.com</footer>
</section>

<section class="card card--back">
  <svg class="abs" style="left:0;top:0" width="340" height="200" viewBox="0 0 340 200">
    <path d="M0 0 H318 C298 60 292 130 300 196 H0 Z" fill="var(--charcoal)"/>
    <path d="M323 0 C303 60 297 130 305 196" fill="none" stroke="var(--orange)" stroke-width="5"/>
  </svg>
  <div class="abs agency-name" style="left:36px;top:56px">The Bramblewood Agency</div>
  <div class="abs headline" style="left:37px;top:100px;font-size:26px">LOREM IPSUM</div>
  <div class="abs website" style="left:38px;top:135px">www.website.com</div>
  <div class="abs" style="left:0;top:196px;width:296px;height:8px;background:var(--orange)"></div>
  <div class="abs" style="left:0;top:204px;width:296px;height:216px;background:linear-gradient(180deg,var(--blue-light),var(--blue))"></div>
  <p class="abs contact" style="left:37px;top:233px">If interested and want more details<br>Please contact:<br>Mirta Dollen @ 555-417-2093</p>
  <div class="photo" role="img" aria-label="Photo: hands with a pen and calculator" style="left:35px;top:318px;width:230px;height:85px;background:linear-gradient(120deg,#f2f4f6,#c9cfd6 55%,#6f7780)"></div>

  <div class="badge" style="left:236px;top:106px;width:116px;height:116px">
    <svg width="116" height="116" viewBox="0 0 116 116"><circle cx="58" cy="58" r="53" fill="#fff" stroke="#c62b2b" stroke-width="2" stroke-dasharray="7 3"/><circle cx="58" cy="58" r="45" fill="#f2f2f2"/></svg>
    <div class="badge-text"><span style="font-size:17px">JOIN US</span><span style="font-size:25px">NOW!</span></div>
  </div>

  <div class="stamp"></div>

  <footer class="footer">lorem ipsum dolor sit amrt | Phone: 123.466.78 | Email: lorem@mailnest.com</footer>
</section>

</body>
</html>
```